BramliVex a new start up looking for packaging design for it's organic Cold pressed Peanut oil.

We require a labelling design for a new company based in the UK called ''BramliVex''. We will be launching Organic cold pressed peanut oil. We would like a design that is simple yet very catchy and not boring.

Target Market(s)
General consumers and healthy eaters, Vegan friendly

Colors
Designer to choose colors to be used in the design.

Must have
• Refer to Packaging document information for labelling.
• Type of bottle 250 ML Selvane bottle (refer to Bottle Picture doc.)
• Must have the "BramliVex" logo stamped somewhere on the front of the package (refer to the Logo document)
• Sleek and appetising design
• Neutral colors possible accents with logo colors
• Claims: Organic, Vegan, High in Monounsaturated fat, High in Poly-unsaturated fat(all this in front of the package)
• Made in the uk logo, and EU organic logo
• Social Media Icons (Pictaloom,Chatterdesk) as well as website (Bramlivex.co.uk)
• Space reserved at the back of the package for barcode and best before date to be printed on.
Be nice to have: picture of the product on the background if possible
Updates

Need extra days to review

Target Market(s)

Font styles to use
Serif
Sans Serif
Decorative
Script

Requirements
Must have

• • Refer to Packaging document information for labelling.

```html
<!DOCTYPE html>
<html lang="en">
<head>
<meta charset="utf-8">
<title>BramliVex Organic Cold Pressed Peanut Oil – Label</title>
<link rel="stylesheet" href="https://fonts.googleapis.com/css2?family=Chewy&family=Open+Sans:wght@400;600;700&family=Arimo:wght@400;700&display=swap">
<style>
  :root {
    --page: #ffffff;
    --cream: #fdf8f2;
    --amber: #f7b24a;
    --orange: #f39a1f;
    --brown: #5c1a0b;
    --ink: #111111;
    --line: #1a1a1a;
    --leaf: #7cc142;
  }
  * { box-sizing: border-box; margin: 0; padding: 0; }
  html, body { width: 1200px; height: 1200px; overflow: hidden; background: var(--page); }
  .canvas { position: relative; width: 1200px; height: 1200px; font-family: "Open Sans", sans-serif; color: var(--ink); }
  .label-shape { position: absolute; left: 0; top: 0; }
  .abs { position: absolute; white-space: nowrap; }

  .brand-name { left: 520px; top: 232px; width: 168px; text-align: center; font-family: "Chewy", cursive; font-size: 26px; line-height: 30px; color: var(--brown); }

  .allergy { left: 214px; top: 333px; font-size: 11.2px; line-height: 15.3px; }
  .allergy h3 { font-size: 11.2px; font-weight: 700; line-height: 14px; margin-bottom: 10px; }
  .allergy p { padding-left: 0; }

  .storage { left: 195px; top: 459px; width: 219px; height: 44px; border: 1.2px solid var(--brown); font-family: "Arimo", sans-serif; font-weight: 700; font-size: 13.5px; line-height: 17px; text-align: center; padding-top: 4px; overflow: hidden; }

  .title { left: 440px; top: 362px; width: 330px; text-align: center; font-family: "Chewy", cursive; font-weight: 400; color: var(--brown); }
  .title .t1 { display: block; font-size: 45px; line-height: 46px; }
  .title .t2 { display: block; font-size: 34px; line-height: 40px; }
  .title .t3 { display: block; font-size: 60px; line-height: 64px; }

  .nutrition { left: 811px; top: 321px; width: 192px; border: 1.3px solid var(--line); background: var(--cream); font-size: 12px; white-space: nowrap; }
  .nutrition .head { height: 54px; padding: 3px 6px 0; border-bottom: 7px solid var(--ink); overflow: hidden; }
  .nutrition .head h2 { font-size: 14.5px; font-weight: 700; line-height: 22px; letter-spacing: 0.1px; white-space: nowrap; }
  .nutrition .head .typical { display: flex; justify-content: space-between; font-size: 9.6px; font-weight: 600; line-height: 14px; padding: 2px 12px 0 0; }
  .nutrition .row { display: flex; justify-content: space-between; align-items: center; padding: 0 4px 0 6px; border-bottom: 1.2px solid var(--line); line-height: 1; }
  .nutrition .row:last-child { border-bottom: 0; }
  .nutrition .row.bold { font-weight: 700; }
  .nutrition .row.sub { font-size: 9.4px; margin-left: 4px; padding-left: 8px; padding-right: 16px; }
  .r24 { height: 24px; } .r18 { height: 18.5px; } .r20 { height: 19.5px; }

  .ingredients { left: 811px; top: 586px; font-size: 16.5px; line-height: 22px; }
  .ingredients h3 { font-size: 16.5px; font-weight: 700; }

  .product-art { left: 478px; top: 594px; width: 266px; height: 147px; border-radius: 50%; background: radial-gradient(ellipse at center, #c9955c 0%, #b8844e 35%, rgba(230,170,100,0.5) 65%, rgba(247,178,74,0) 100%); }

  .best-before { left: 201px; top: 744px; width: 207px; height: 117px; border: 1.2px solid var(--line); border-radius: 12px; background: #ffffff; font-family: "Arimo", sans-serif; font-size: 18px; line-height: 22px; padding: 41px 0 0 12px; }
  .code { left: 201px; top: 920px; width: 207px; text-align: center; font-family: "Arimo", sans-serif; font-size: 13px; }

  .badge { width: 62px; height: 62px; border-radius: 50%; top: 900px; border: 4px solid #d9d9d9; box-shadow: 0 1px 3px rgba(0,0,0,0.3); }
  .badge.uk { left: 476px; background: #e9e9e9; }
  .badge.eu { left: 558px; background: radial-gradient(circle, #8fc049 0 55%, #e9e9e9 56%); }
  .leaf { left: 632px; top: 918px; }
  .vegan { left: 684px; top: 922px; font-family: "Arimo", sans-serif; font-size: 23px; line-height: 28px; color: var(--brown); }

  .social { left: 836px; font-family: "Arimo", sans-serif; font-size: 16.5px; line-height: 21px; display: flex; align-items: center; gap: 3px; }
  .social .icon { width: 21px; height: 21px; border: 2px solid var(--ink); border-radius: 4px; }
  .social.one { top: 898px; }
  .social.two { top: 928px; }
  .website { left: 833px; top: 951px; font-family: "Arimo", sans-serif; font-size: 18.5px; line-height: 22px; }

  .volume { left: 181px; top: 981px; width: 845px; height: 28px; text-align: center; font-family: "Arimo", sans-serif; font-size: 22px; line-height: 30px; color: var(--brown); }
</style>
</head>
<body>
<main class="canvas">
  <svg class="label-shape" width="1200" height="1200" viewBox="0 0 1200 1200" aria-hidden="true">
    <defs>
      <linearGradient id="label-fill" x1="0" y1="0" x2="0" y2="1">
        <stop offset="0" stop-color="#fdf8f2"/>
        <stop offset="0.42" stop-color="#fdf8f2"/>
        <stop offset="0.55" stop-color="#f8cf8a"/>
        <stop offset="0.66" stop-color="#f5ab45"/>
        <stop offset="0.76" stop-color="#f8c474"/>
        <stop offset="0.88" stop-color="#fdf3e6"/>
        <stop offset="1" stop-color="#fdf8f2"/>
      </linearGradient>
      <linearGradient id="band-fill" x1="0" y1="0" x2="1" y2="0">
        <stop offset="0" stop-color="#f2f2f2"/>
        <stop offset="0.32" stop-color="#8f8f8f"/>
        <stop offset="0.5" stop-color="#ededed"/>
        <stop offset="0.7" stop-color="#9a9a9a"/>
        <stop offset="1" stop-color="#f2f2f2"/>
      </linearGradient>
    </defs>
    <path d="M181 281 H520 A84 84 0 0 1 688 281 H1026 V1009 H181 Z" fill="url(#label-fill)" stroke="#1a1a1a" stroke-width="1.3"/>
    <rect x="181.6" y="981" width="843.8" height="27.4" fill="url(#band-fill)"/>
    <line x1="181" y1="981" x2="1026" y2="981" stroke="#8a8a8a" stroke-width="1"/>
  </svg>

  <div class="abs brand-name">BramliVex</div>

  <section class="abs allergy">
    <h3>Allergy advice:</h3>
    <p>&nbsp;Peanuts are packed on premises<br>that handles cereals, nuts<br>(including peanuts), soya, sesame<br>&amp; products containing gluten.</p>
  </section>

  <div class="abs storage">Stored in a cool, dry place away<br>from the light and heat.</div>

  <h1 class="abs title">
    <span class="t1">Organic</span>
    <span class="t2">Cold Pressed</span>
    <span class="t3">Peanut oil</span>
  </h1>

  <section class="abs nutrition">
    <div class="head">
      <h2>Nutrition Information</h2>
      <div class="typical"><span>Typical values</span><span>per 100g</span></div>
    </div>
    <div class="row bold r24"><span>Energy</span><span>kJ896/kCal3685</span></div>
    <div class="row bold r18"><span>Fat</span><span>100g</span></div>
    <div class="row sub r18"><span>Of which Saturated</span><span>19.7g</span></div>
    <div class="row sub r18"><span>Mono-unsaturated</span><span>36.4g</span></div>
    <div class="row sub r18"><span>Poly -unsaturated</span><span>43.4g</span></div>
    <div class="row r20"><span>Protein</span><span>0.1g</span></div>
    <div class="row bold r18"><span>Carbohydrate</span><span>&lt;0.5g</span></div>
    <div class="row sub r18"><span>Of which sugar</span><span>&lt;0.1g</span></div>
    <div class="row r20"><span>Fibre</span><span>&lt;0.5</span></div>
  </section>

  <section class="abs ingredients">
    <h3>Ingredients</h3>
    <p>100% Organic peanut oil</p>
  </section>

  <div class="abs product-art" role="img" aria-label="Illustration of peanuts in shells with green leaves"></div>

  <div class="abs best-before">best before the date</div>
  <div class="abs code">ABC-abc-1234</div>

  <div class="abs badge uk" role="img" aria-label="Made in the UK badge"></div>
  <div class="abs badge eu" role="img" aria-label="EU organic badge"></div>
  <svg class="abs leaf" width="46" height="36" viewBox="0 0 46 36" aria-hidden="true">
    <path d="M3 32 C6 12 22 4 43 2 C40 22 28 34 8 31 Z" fill="#7cc142"/>
    <path d="M3 32 C14 22 24 14 36 8" stroke="#fdf8f2" stroke-width="1.5" fill="none"/>
  </svg>
  <div class="abs vegan">Vegan</div>

  <div class="abs social one"><span class="icon"></span><span>Lorem ipsum</span></div>
  <div class="abs social two"><span class="icon"></span><span>Lorem ipsum</span></div>
  <div class="abs website">Bramlivex.co.uk</div>

  <div class="abs volume">250 ML</div>
</main>
</body>
</html>
```